Coffee Roaster Needs A Postcard Design

I am coffee roaster ( a home business) and I would like to create a neighborhood delivery service. Once a month I would delivery fresh roasted coffee to my neighbors. I would like to create a postcard to advertise the coffee delivery service.

Preferences: The postcard would be very simple, primarily black and white ( a little color) with visuals; fresh roasted coffee beans, delivered to the doorstep, a great cup of coffee. Simple steps, 1 2 & 3.

I have a website the postcard advertisement should flow with the site : www.brambledgebeanworks.com

Target Market(s)

Upper class residential neighborhood

Industry/Entity Type

Business

Font styles to use
Serif

Colors
f04a50

Requirements
Must have
• Images _ Coffee Beans

```html
<!DOCTYPE html>
<html lang="en">
<head>
<meta charset="utf-8">
<title>Brambledge Bean Works – Neighborhood Coffee Delivery</title>
<link rel="stylesheet" href="https://fonts.googleapis.com/css2?family=Jost:wght@300;400&display=swap">
<style>
  :root {
    --ink: #ffffff;
    --icon: #4a4038;
    --disc: #f4f2ef;
    --sepia-light: #dcd7cf;
    --sepia-mid: #8b7b6c;
    --sepia-dark: #3e3229;
    --wood: #b9a996;
  }
  * { margin: 0; padding: 0; box-sizing: border-box; }
  html, body { width: 1200px; height: 932px; overflow: hidden; }
  body { font-family: "Jost", "Futura", sans-serif; color: var(--ink); }
  .postcard { position: relative; width: 1200px; height: 932px; overflow: hidden; }
  .bean-photo {
    position: absolute; inset: 0;
    background:
      radial-gradient(ellipse 55% 30% at 55% 45%, rgba(62,50,41,.85), rgba(62,50,41,0) 70%),
      radial-gradient(ellipse 40% 28% at 70% 72%, rgba(70,56,45,.75), rgba(70,56,45,0) 70%),
      radial-gradient(ellipse 35% 25% at 30% 60%, rgba(90,74,60,.6), rgba(90,74,60,0) 70%),
      linear-gradient(180deg, var(--sepia-light) 0%, #c9c1b6 18%, var(--sepia-mid) 45%, #6f6052 70%, var(--wood) 100%);
  }
  .content { position: absolute; inset: 0; text-align: center; }
  .headline {
    position: absolute; top: 186px; left: 0; right: 0;
    font-weight: 400; font-size: 58px; line-height: 76px; letter-spacing: 1px;
  }
  .steps { position: absolute; top: 396px; left: 0; right: 0; height: 200px; }
  .step { position: absolute; width: 220px; text-align: center; }
  .step .disc {
    width: 114px; height: 114px; border-radius: 50%; background: var(--disc);
    margin: 0 auto; display: flex; align-items: center; justify-content: center;
  }
  .step .caption {
    margin-top: 20px; font-weight: 300; font-size: 22px; line-height: 30px; letter-spacing: 2px;
  }
  .step-beans { left: 272px; }
  .step-delivery { left: 492px; }
  .step-cup { left: 707px; }
  .operator { position: absolute; top: 30px; font-size: 48px; font-weight: 300; line-height: 50px; }
  .op-plus { left: 477px; }
  .op-equals { left: 694px; }
  .brand-name {
    position: absolute; top: 728px; left: 0; right: 0;
    font-weight: 400; font-size: 32px; letter-spacing: 2px; text-transform: uppercase;
  }
  .web-address {
    position: absolute; top: 789px; left: 50%; transform: translateX(-50%);
    border: 1.5px solid var(--ink); padding: 0 14px; height: 54px; line-height: 52px;
    font-weight: 300; font-size: 26px; letter-spacing: 1.5px; white-space: nowrap;
  }
</style>
</head>
<body>
<main class="postcard">
  <div class="bean-photo" role="img" aria-label="Sepia close-up photograph of roasted coffee beans scattered on a wooden board"></div>
  <div class="content">
    <h1 class="headline">Fresh Roasted Coffee Beans<br>Delivered Right to your Doorstep</h1>

    <section class="steps">
      <div class="step step-beans">
        <div class="disc">
          <svg width="60" height="60" viewBox="0 0 60 60" aria-hidden="true">
            <g fill="var(--icon)">
              <ellipse cx="34" cy="15" rx="13" ry="9" transform="rotate(-20 34 15)"/>
              <ellipse cx="20" cy="38" rx="9" ry="13" transform="rotate(15 20 38)"/>
              <ellipse cx="42" cy="40" rx="9" ry="13" transform="rotate(-10 42 40)"/>
            </g>
            <g fill="none" stroke="var(--disc)" stroke-width="2">
              <path d="M23 18 q11 -2 22 -6"/>
              <path d="M19 26 q4 12 2 24"/>
              <path d="M43 28 q-3 12 0 24"/>
            </g>
          </svg>
        </div>
        <p class="caption">Locally Roasted<br>Coffee Beans</p>
      </div>

      <span class="operator op-plus" aria-hidden="true">+</span>

      <div class="step step-delivery">
        <div class="disc">
          <svg width="72" height="44" viewBox="0 0 72 44" aria-hidden="true">
            <g fill="none" stroke="var(--icon)" stroke-width="2.2" stroke-linecap="round" stroke-linejoin="round">
              <circle cx="14" cy="29" r="11"/>
              <circle cx="58" cy="29" r="11"/>
              <path d="M14 29 L25 12 L48 12 L36 29 Z"/>
              <path d="M25 12 L22 5 M18 5 L27 5"/>
              <path d="M48 12 L58 29 M48 12 L46 5 L52 5"/>
            </g>
          </svg>
        </div>
        <p class="caption">Delivered to<br>Your Doorstep</p>
      </div>

      <span class="operator op-equals" aria-hidden="true">=</span>

      <div class="step step-cup">
        <div class="disc">
          <svg width="60" height="70" viewBox="0 0 60 70" aria-hidden="true">
            <g fill="none" stroke="var(--icon)" stroke-width="1.8" stroke-linecap="round">
              <path d="M22 18 q-4 -5 0 -9 q4 -4 0 -8"/>
              <path d="M30 18 q-4 -5 0 -9 q4 -4 0 -8"/>
            </g>
            <path d="M8 26 H46 V44 a14 14 0 0 1 -14 14 H22 a14 14 0 0 1 -14 -14 Z" fill="var(--icon)"/>
            <path d="M46 31 h3 a7 7 0 0 1 0 14 h-4" fill="none" stroke="var(--icon)" stroke-width="4"/>
            <rect x="4" y="62" width="46" height="3" fill="var(--icon)"/>
          </svg>
        </div>
        <p class="caption">A Great Cup<br>of Coffee</p>
      </div>
    </section>

    <h2 class="brand-name">Brambledge Bean Works</h2>
    <p class="web-address">brambledgebeanworks.com</p>
  </div>
</main>
</body>
</html>
```